Professional Lighting Providers - Web Design

We need a web design to showcase our ability to provide lighting design and equipment to those who are in need of lighting equipment.

Our 4 markets are:
Broadcasting - Public and Commercial
Education - ISD wide, and private schools
Government - National News, Chamber videos, Press Releases
Religious - Sermon Recording, etc.

We provide lighting products, design consultations(how lights are setup and such), and custom light work.

We want the home page to be setup in a way that someone in one of the 4 markets can drill down into the site. Meaning they are greeted on the home page with 4 large icons or pictures for each market and then they can go farther into the site. We also want a top navigation to be preset so people who are just looking for lighting can also browse our products.

Logo colors are not as they appear on our current website.
#383388 is our current logo color, please also see attachment of logo. In addition, we are just "Clear Beam - Lighting Systems". We dropped the RZ7 out of our name so please don't use it in the concept.

Our Current Site is http://rz7-example.com/index.asp.
We don't have set colors but we know we do not want reds or yellows.

The design should be simple, not cluttered, and not artsy, not fun, but very serious.

Requirements
Must have
• Image banner/slider at the top that slides our 4 products.
Also need to have a form on the home page that will convert visitors to subscribers for a newsletter. Also on every page we want a form were people can send an email off to us asking questions.

```html
<!DOCTYPE html>
<html lang="en">
<head>
<meta charset="utf-8">
<title>Clear Beam Lighting Systems</title>
<link rel="stylesheet" href="https://fonts.googleapis.com/css2?family=Arimo:wght@400;700&family=PT+Sans:wght@400;700&family=PT+Sans+Narrow:wght@700&display=swap">
<style>
:root{
  --brand:#383388;
  --brand-deep:#3d3590;
  --banner-top:#6a62c6;
  --banner-bottom:#3f3692;
  --side-grey:#6e6e6e;
  --leaf:#8db23a;
  --leaf-bright:#9cc31c;
  --rule:#cfd0c0;
  --ink:#333333;
  --footer-bg:#f0f0f0;
  --white:#ffffff;
}
*{box-sizing:border-box;margin:0;padding:0}
html,body{width:1200px;height:1162px;overflow:hidden;background:var(--white)}
body{font-family:"Arimo",Arial,sans-serif;color:var(--ink);position:relative}
.abs{position:absolute}
.top-strip{left:0;top:0;width:1200px;height:6px;background:#e6e6e6}
.main-nav{left:0;top:46px;width:1200px;display:flex;justify-content:center;gap:0;font:700 14px/18px "Arimo",sans-serif;color:#222}
.main-nav a{color:inherit;text-decoration:none;padding:0 14px;border-left:1px dotted #c8c8c8}
.main-nav a:first-child{border-left:none}
.banner{left:0;top:95px;width:1200px;height:312px;background:var(--side-grey)}
.brand-panel{left:46px;top:0;width:243px;height:312px;background:linear-gradient(#fff,#f2f2f2 60%,#d9d9d9);text-align:center}
.brand-name{position:absolute;left:0;right:0;top:98px;display:flex;align-items:center;justify-content:center;gap:8px;font:700 26px/1 "Arimo",sans-serif;color:var(--brand)}
.brand-name i{width:22px;height:22px;background:var(--brand);display:block}
.brand-sub{position:absolute;left:0;right:0;top:132px;font:400 15px/1 "Arimo",sans-serif;letter-spacing:2px;color:#333}
.tagline{position:absolute;left:0;right:0;top:178px;font:400 17px/28px "PT Sans",sans-serif;color:var(--brand)}
.slider{left:289px;top:0;width:869px;height:312px;background:linear-gradient(var(--banner-top),var(--banner-bottom))}
.tile{position:absolute;top:46px;height:120px;background:var(--white);border-radius:8px;padding:8px}
.tile .shot{width:100%;height:100%;border-radius:4px;background:linear-gradient(#e9e9e9,#bdbdbd)}
.tile-glow{position:absolute;top:174px;height:55px;border-radius:8px;background:linear-gradient(rgba(255,255,255,.14),rgba(255,255,255,0))}
.tile-label{position:absolute;top:183px;text-align:center;font:700 18px/24px "PT Sans Narrow",sans-serif;color:var(--white)}
.pager{position:absolute;top:264px;width:28px;height:25px;border-radius:3px;background:linear-gradient(#fff,#c9c9c9);font:700 15px/25px "Arimo",sans-serif;text-align:center;color:#222}
.pager.is-active{background:linear-gradient(#eef7c4,#b9d65a)}
.section-title{font:400 33px/1 "PT Sans",sans-serif;color:var(--brand)}
.section-rule{height:3px;background:var(--rule)}
.product-shot{background:linear-gradient(90deg,#2b2b2b,#8a8a8a 40%,#e8e8e8 60%,#333);border-radius:3px}
.news-shot{background:radial-gradient(circle at 50% 50%,#8c8c8c,#2b2b2b 70%,#fff 71%)}
.lead{font:400 21px/25px "Arimo",sans-serif;color:var(--leaf)}
.features{list-style:none;font:400 15.5px/23.4px "Arimo",sans-serif;color:#333}
.features li{position:relative;padding-left:26px}
.features svg{position:absolute;left:0;top:6px}
.read-more{font:700 15px/1 "Arimo",sans-serif;letter-spacing:.5px;color:#111}
.footer-band{left:0;top:853px;width:1200px;height:194px;background:var(--footer-bg)}
.foot-head{font:700 15px/1 "Arimo",sans-serif;color:var(--leaf-bright)}
.foot-list{list-style:none;font:400 15.5px/23.4px "Arimo",sans-serif;color:#222}
.foot-links{list-style:none;font:400 14px/23.4px "Arimo",sans-serif;color:#222}
.field-label{font:400 15px/1 "Arimo",sans-serif;color:#222}
.field{background:var(--white);width:183px;height:29px}
.submit{background:var(--leaf-bright);color:var(--white);font:400 16px/24px "Arimo",sans-serif;text-align:center;width:63px;height:24px}
.bottom-band{left:0;top:1047px;width:1200px;height:99px;background:var(--brand-deep)}
.bottom-brand{left:83px;top:12px;width:216px;height:76px;background:var(--white);text-align:center}
.bottom-brand .brand-name{top:17px;font-size:23px}
.bottom-brand .brand-name i{width:18px;height:18px}
.bottom-brand .brand-sub{top:48px;font-size:14px}
.copyright{left:491px;top:67px;font:700 15px/1 "Arimo",sans-serif;color:var(--white)}
.follow{left:967px;top:24px;font:700 15px/1 "Arimo",sans-serif;color:var(--white)}
.social{top:51px;width:33px;height:33px;border-radius:50%;background:linear-gradient(#e2e2e2,#9a9a9a)}
</style>
</head>
<body>
<div class="abs top-strip"></div>
<nav class="abs main-nav">
  <a href="#">HOME</a><a href="#">WHY US?</a><a href="#">RESUME</a><a href="#">PRODUCTS</a><a href="#">LIGHTING DESIGN/QUOTE</a><a href="#">REQUEST</a><a href="#">ABOUT US</a><a href="#">LATEST NEWS</a><a href="#">MANUALS</a><a href="#">TECHNICAL</a>
</nav>

<section class="abs banner">
  <div class="abs brand-panel">
    <div class="brand-name"><i></i>Clear Beam</div>
    <div class="brand-sub">Lighting Systems</div>
    <div class="tagline">REAL SOLUTIONS TO<br>STUDIO LIGHTING</div>
  </div>
  <div class="abs slider">
    <div class="tile" style="left:32px;width:149px"><div class="shot" role="img" aria-label="Accent light fixture"></div></div>
    <div class="tile" style="left:189px;width:272px"><div class="shot" role="img" aria-label="Video conference light bars and panel"></div></div>
    <div class="tile" style="left:470px;width:150px"><div class="shot" role="img" aria-label="Portable lights on stands with case"></div></div>
    <div class="tile" style="left:630px;width:202px"><div class="shot" role="img" aria-label="Fill light panels"></div></div>
    <div class="tile-glow" style="left:32px;width:149px"></div>
    <div class="tile-glow" style="left:189px;width:272px"></div>
    <div class="tile-glow" style="left:470px;width:150px"></div>
    <div class="tile-glow" style="left:630px;width:202px"></div>
    <div class="tile-label" style="left:32px;width:149px;top:188px">ACCENT LIGHTS</div>
    <div class="tile-label" style="left:189px;width:272px">VIDEO CONFERENCE &amp;<br>SMALL STUDIO LIGHTS</div>
    <div class="tile-label" style="left:470px;width:150px;top:195px">PORTABLE</div>
    <div class="tile-label" style="left:630px;width:202px;top:195px">FILL LIGHTS</div>
    <div class="pager is-active" style="left:658px">1</div>
    <div class="pager" style="left:693px">2</div>
    <div class="pager" style="left:728px">3</div>
    <div class="pager" style="left:763px">4</div>
    <div class="pager" style="left:798px">5</div>
  </div>
</section>

<svg width="0" height="0" style="position:absolute"><defs><symbol id="tick" viewBox="0 0 14 12"><path d="M1 6.5l4 4L13 1.5" fill="none" stroke="#8db23a" stroke-width="2.6"/></symbol></defs></svg>

<h2 class="abs section-title" style="left:59px;top:457px">Featured Products</h2>
<div class="abs section-rule" style="left:55px;top:503px;width:600px"></div>
<div class="abs product-shot" role="img" aria-label="LED studio light panel" style="left:70px;top:548px;width:147px;height:228px"></div>
<p class="abs lead" style="left:244px;top:535px;width:403px;text-align:justify">Studio or Council Chamber LED Lighting Solutions</p>
<ul class="abs features" style="left:250px;top:604px">
  <li><svg width="14" height="12"><use href="#tick"/></svg>Long throw</li>
  <li><svg width="14" height="12"><use href="#tick"/></svg>Low heat &amp; low electrical draw</li>
  <li><svg width="14" height="12"><use href="#tick"/></svg>31w or 77w</li>
  <li><svg width="14" height="12"><use href="#tick"/></svg>11 or 45 bare beam spread</li>
  <li><svg width="14" height="12"><use href="#tick"/></svg>Tungsten or Daylight</li>
  <li><svg width="14" height="12"><use href="#tick"/></svg>Instant "on"</li>
  <li><svg width="14" height="12"><use href="#tick"/></svg>Dimmable, daily chain power</li>
</ul>
<a class="abs read-more" style="left:566px;top:824px">Read More</a>

<h2 class="abs section-title" style="left:729px;top:461px">Latest News</h2>
<div class="abs section-rule" style="left:727px;top:506px;width:435px"></div>
<p class="abs lead" style="left:728px;top:540px;font-size:20px">Introducing the 4CB560</p>
<p class="abs" style="left:732px;top:573px;font:700 15px/1 Arimo,sans-serif;color:#333">Same price as the 2CB560, but</p>
<div class="abs news-shot" role="img" aria-label="Two LED light bank fixtures" style="left:709px;top:607px;width:164px;height:180px"></div>
<ul class="abs features" style="left:888px;top:616px;width:270px;text-align:justify">
  <li><svg width="14" height="12"><use href="#tick"/></svg>More light output</li>
  <li><svg width="14" height="12"><use href="#tick"/></svg>More even distribution of light</li>
  <li><svg width="14" height="12"><use href="#tick"/></svg>Lighter aluminum construction</li>
  <li><svg width="14" height="12"><use href="#tick"/></svg>Semi-specular reflector</li>
  <li><svg width="14" height="12"><use href="#tick"/></svg>Inner two-lamp, outer-two lamp, all four lamp bank switchability</li>
  <li><svg width="14" height="12"><use href="#tick"/></svg>Vertical or horizontal mounting</li>
</ul>
<a class="abs read-more" style="left:1066px;top:824px">Read More</a>

<footer>
  <div class="abs footer-band">
    <h3 class="abs foot-head" style="left:82px;top:18px">PRODUCTS</h3>
    <ol class="abs foot-list" style="left:79px;top:41px">
      <li>1. BROADCAST VIDEO STUDIOS</li>
      <li>2. CYC WALLS</li>
      <li>3. VIDEO CONFERENCE</li>
      <li>4. WORSHIP SERVICES</li>
      <li>BROADCAST</li>
      <li>5.VIDEO EDUCATION STUDIOS</li>
    </ol>
    <h3 class="abs foot-head" style="left:492px;top:18px">HOME</h3>
    <ul class="abs foot-links" style="left:492px;top:41px">
      <li>WHY US?</li><li>RESUME</li><li>PRODUCTS</li><li>LIGHTING DESIGN/QUOTE</li><li>REQUEST</li><li>ABOUT US</li>
    </ul>
    <h3 class="abs foot-head" style="left:793px;top:18px">CONTACT US</h3>
    <form>
      <label class="abs field-label" style="left:796px;top:51px">Name:</label>
      <div class="abs field" style="left:853px;top:45px"></div>
      <label class="abs field-label" style="left:796px;top:88px">Email:</label>
      <div class="abs field" style="left:853px;top:81px"></div>
      <label class="abs field-label" style="left:796px;top:124px">Phone:</label>
      <div class="abs field" style="left:853px;top:118px"></div>
      <div class="abs submit" style="left:860px;top:155px">Submit</div>
    </form>
  </div>
  <div class="abs bottom-band">
    <div class="abs bottom-brand">
      <div class="brand-name"><i></i>Clear Beam</div>
      <div class="brand-sub">Lighting Systems</div>
    </div>
    <p class="abs copyright">Copyrights Reserved 2012. Clear Beam</p>
    <p class="abs follow">FOLLOW US</p>
    <span class="abs social" style="left:967px"></span>
    <span class="abs social" style="left:1012px"></span>
    <span class="abs social" style="left:1058px"></span>
    <span class="abs social" style="left:1103px"></span>
  </div>
</footer>
</body>
</html>
```